Launchpad Ledger: Turning your early capital into a sprint of expansion

I need a full-color book cover for a paperback (front, spine and back) in high resolution InDesign and PDF. I also need the derived version for an e-book. Here are some briefing elements:

Audience Profile
Imagine a person standing at the threshold of a significant milestone in their entrepreneurial journey, their heart a mix of excitement and anxiety. Having just secured Series A funding, they acknowledge the validation of their relentless effort and vision but are deeply conscious of the daunting challenges that lie ahead. This individual is navigating the complexities of rapid scaling, managing a larger and potentially more demanding board of directors, and restructuring the company's priorities while preserving its culture. The weight of expectations to succeed and propel the startup to new heights is palpable, stirring a sense of overwhelm amidst the triumph.

Reader Situation
The current state of our target reader might be a mix of excitement and anxiety. Having just secured Series A funding, they recognize the validation of their hard work and vision but are acutely aware of the mountain of challenges ahead. They may feel overwhelmed by the expectations to scale rapidly, manage a larger and potentially more demanding board of directors, and restructure the company's priorities while maintaining its culture. After reading this book and implementing its advice, they would feel empowered, equipped with a clear strategy for tackling the challenges that come with Series A funding, and confident in their ability to scale their startup efficiently. They will be on a promising path toward achieving growth targets necessary for a successful Series B raise, with a newfound understanding of how to manage their team and board dynamics effectively.
Updates

Got some good first attempts on the first round of submissions, I like many of the color schemes proposed and some people have submitted abstract pictures that chime really well with founders who are trying to grow the company.
Where many people fall short is in "Launchpad ledger" not being the most prominent title on the cover page, picking a picture that does not particularly chime with founders trying to reach higher growth for their company, and sometimes in just throwing some elements on a page and hoping something sticks :)
I'm actively reviewing 3 times per day so please try to follow the briefing and get to the top of the selection list.

Hello everybody, thank you for the designs coming in. There are some entries that are showing great potential! Some clarifications:

- "Series A" and by extension "Launchpad Ledger" should really be the most prominent part of the cover. If you split it up, make sure "Series A" is together on the same line as it is a term founders will (and must) recognize. If you use different sizes, make sure "Series A" is bigger than "Playbook"
- I much prefer the designs with simpler, more abstract pictures, eg an outline of a person is better than a detailed drawing of a person, but a drawing is still better than a photograph
- Some of you have been using very well known stock photos, we want this to be unique so those designs will not be favored.
- If you do have a person on the cover evoking a startup founder, then put them in clothes that people will recognize: typically a hoody, a tshirt with the logo of their startup, jeans or other comfortable pants, and sneakers. Do not put someone in a suit and tie.
- If you can, use the "footer bar" supplied at the bottom of the front cover to evoke our branding. You can just use the color bars, the logo can be somewhere else.
- The logo should be relatively small and we prefer it to be on the right (because of the arrow in the logo). It should be less prominent than the author name (Tobias Wrenfield)
- Finally, I am starting to play closer attention to the spine and the back cover. Spine should be attractive and make it easy to find the book, with author name, title and the Corvell Academy logo (or just the icon). Back cover should have room for a summary, lots of testimonial quotes, a picture of the author and a bar code.

I will check designs daily and give feedback for every design submitted. Thank you all for putting in great work and I'm looking forward to picking a cover shortly!

Target Market(s)

Founders and employees of technology startups in North America, Europe and East Asia

Industry/Entity Type

Startups, technology, software

Font styles to use
Sans Serif

Requirements
Must have
• Dominant title, simple (conceptual) picture, look and feel of practical business book, attractive back cover inviting people to read quotes
Nice to have
• Picture on the front cover that evokes the feeling of having a guide, a map, a navigation tool, so that even if you don't know the exact road, you'll be all right. But ideally keep the picture more abstract and conceptual, I'm not looking for an elaborate illustration
Should not have
• Elaborate illustration, photo on the front cover, complex color scheme

```html
<!DOCTYPE html>
<html lang="en">
<head>
<meta charset="utf-8">
<title>Launchpad Ledger — Book Cover</title>
<link rel="stylesheet" href="https://fonts.googleapis.com/css2?family=League+Gothic&family=Barlow+Semi+Condensed:wght@500;600&display=swap">
<style>
  :root {
    --page: #ffffff;
    --navy: #0c4a6d;
    --gold: #e09b2a;
    --sage: #97b36b;
    --ember: #e0622f;
    --white: #ffffff;
    --art-a: #a6cc46;
    --art-b: #f0763c;
  }
  html, body {
    margin: 0;
    width: 1200px;
    height: 1200px;
    overflow: hidden;
    background: var(--page);
  }
  .cover {
    position: absolute;
    left: 248px;
    top: 74px;
    width: 687px;
    height: 1048px;
    background: var(--navy);
    overflow: hidden;
  }
  .subtitle {
    position: absolute;
    top: 52px;
    left: 0;
    width: 100%;
    margin: 0;
    text-align: center;
    color: var(--white);
    font-family: "Barlow Semi Condensed", sans-serif;
    font-weight: 500;
    font-size: 25px;
    line-height: 35px;
    letter-spacing: 3.2px;
    text-transform: uppercase;
  }
  .title {
    position: absolute;
    left: 0;
    top: 0;
    width: 687px;
    height: 1048px;
  }
  .title text {
    font-family: "League Gothic", sans-serif;
    fill: var(--gold);
  }
  .growth-art {
    position: absolute;
    left: 106px;
    top: 900px;
    width: 330px;
    height: 133px;
    background: linear-gradient(90deg, var(--gold) 0%, var(--art-a) 45%, var(--art-b) 100%);
    opacity: 0.9;
  }
  .publisher {
    position: absolute;
    left: 490px;
    top: 890px;
    width: 150px;
    text-align: center;
    color: var(--white);
    font-family: "Barlow Semi Condensed", sans-serif;
    font-weight: 600;
  }
  .publisher-mark {
    display: block;
    width: 40px;
    height: 40px;
    margin: 0 auto 10px;
    border: 3px solid var(--white);
    box-sizing: border-box;
  }
  .publisher-name {
    display: block;
    font-size: 28px;
    line-height: 28px;
    letter-spacing: 0.5px;
  }
  .publisher-sub {
    display: block;
    font-size: 10px;
    letter-spacing: 6.5px;
    margin-top: 3px;
  }
  .footer-bar {
    position: absolute;
    left: 0;
    bottom: 0;
    width: 100%;
    height: 15px;
    display: flex;
  }
  .footer-bar span:nth-child(1) { width: 106px; background: var(--sage); }
  .footer-bar span:nth-child(2) { width: 432px; background: var(--gold); }
  .footer-bar span:nth-child(3) { flex: 1; background: var(--ember); }
</style>
</head>
<body>
  <main class="cover">
    <p class="subtitle">Turning your early capital into<br>a sprint of expansion</p>

    <svg class="title" viewBox="0 0 687 1048" aria-label="Launchpad Ledger">
      <text x="60" y="301" font-size="196" textLength="555" lengthAdjust="spacingAndGlyphs">LAUNCH</text>
      <text x="60" y="566" font-size="336" textLength="555" lengthAdjust="spacingAndGlyphs">PAD</text>
      <text x="60" y="836" font-size="336" textLength="555" lengthAdjust="spacingAndGlyphs">LEDGER</text>
    </svg>

    <div class="growth-art" role="img" aria-label="Illustration of coin stacks, banknotes and a money bag along a rising green growth arrow"></div>

    <div class="publisher">
      <span class="publisher-mark"></span>
      <span class="publisher-name">CORVELL</span>
      <span class="publisher-sub">ACADEMY</span>
    </div>

    <div class="footer-bar"><span></span><span></span><span></span></div>
  </main>
</body>
</html>
```